Harbor Crest Vitality.com Landing Page

Create a well designed home/landing page using that communicates the feeling of Harbor Crest Vitality with this sections that scroll from top to bottom -
Top section - Displays "Harbor Crest Vitality" with space for embedded YouTube video.

The following sections follow the top section -
Assess your current Harbor Crest Vitality. Complete our free life balance assessment to identify key areas where you you will most benefit.
"Learn more" call to action button

Create a Harbor Crest Vitality Learning Portal account. Get a 14 day free trial to a wealth of learning activities, motivational videos and professional presentations on our learning portal designed specifically to address the eight essential areas of Harbor Crest Vitality.
"Register now" call to action button

Get weekly reports on your progress and goal achievement. Celebrate your success each week as you review your progress on each life balance area.

Appropriate royalty free photos and graphics that fit the chosen theme you recommend.

I'm reviewing the designs. I realize that I need to clarify that Harbor Crest Vitality focuses on eight areas, not just physical fitness and meditation. Spirituality and Sense of Purpose; Fitness and Health; Relationships; Personal Finance; Recreation and Fun; Physical Environment; Personal Development and Learning; Work and Career

1 page

33a6d7
00a990
9bcb3c
2f73b3

```html
<!DOCTYPE html>
<html lang="en">
<head>
<meta charset="utf-8">
<title>Harbor Crest Vitality</title>
<link rel="stylesheet" href="https://fonts.googleapis.com/css2?family=Montserrat:wght@500;600;700&family=Raleway:wght@300;400;500;600&display=swap">
<style>
  :root {
    --sky-blue: #33a6d7;
    --ocean-blue: #2f73b3;
    --lime: #9bcb3c;
    --teal: #00a990;
    --white: #ffffff;
    --ink: #0b0f0e;
    --accent-red: #ff2a2a;
  }
  * { margin: 0; padding: 0; box-sizing: border-box; }
  html, body { width: 1200px; height: 2511px; overflow: hidden; background: var(--ink); }
  body { position: relative; font-family: "Raleway", sans-serif; color: var(--white); }

  .hero { position: absolute; left: 0; top: 0; width: 1200px; height: 604px;
    background: radial-gradient(ellipse at 72% 40%, #3d3a33 0%, #1d221d 40%, #0e1311 75%), #0e1311; }
  .hero-backdrop { position: absolute; inset: 0;
    background: linear-gradient(180deg, rgba(10,14,12,0.2) 0%, rgba(40,44,36,0.55) 70%, rgba(70,72,64,0.7) 100%); }
  .menu-toggle { position: absolute; left: 1119px; top: 40px; width: 36px; height: 16px; }
  .hero-title { position: absolute; left: 134px; top: 220px; width: 476px; text-align: center;
    font-family: "Raleway", sans-serif; font-weight: 300; font-size: 43px; letter-spacing: -0.5px; }
  .watch-label { position: absolute; left: 300px; top: 287px; width: 145px; text-align: center;
    font-size: 15px; font-weight: 400; }
  .play-button { position: absolute; left: 342px; top: 312px; width: 61px; height: 61px; }
  .hero-photo { position: absolute; left: 745px; top: 63px; width: 319px; height: 479px;
    border: 2px solid rgba(255,255,255,0.75);
    background: linear-gradient(180deg, #4c6a48 0%, #7c8d80 35%, #b9bdb4 55%, #56663e 75%, #4c4a3e 100%); }

  .section { position: absolute; left: 0; width: 1200px; }
  .assess { top: 604px; height: 604px;
    background: linear-gradient(180deg, #98a29a 0%, #a79a7a 25%, #5d6a7a 48%, #3f4a44 70%, #2d3a26 100%); }
  .assess-copy { position: absolute; left: 531px; top: 100px; width: 600px; }
  .heading { font-family: "Montserrat", sans-serif; font-weight: 600; line-height: 1.08; }
  .assess .heading { font-size: 35px; line-height: 42px; letter-spacing: 0.3px; }
  .assess .lede { margin-top: 40px; font-family: "Montserrat", sans-serif; font-weight: 600;
    font-size: 19px; line-height: 30px; }
  .cta { display: block; position: absolute; width: 218px; height: 66px; line-height: 66px; text-align: center;
    font-family: "Raleway", sans-serif; font-weight: 600; font-size: 19px; color: var(--white); text-decoration: none; }
  .cta-ocean { background: var(--ocean-blue); left: 531px; top: 370px; }

  .portal { top: 1208px; height: 602px;
    background: linear-gradient(180deg, #56605f 0%, #6f8a93 35%, #5e97a8 60%, #3f7f95 85%, #2e6a7a 100%); }
  .portal-card { position: absolute; left: 73px; top: 1148px; width: 700px; height: 512px;
    background: var(--sky-blue); box-shadow: 0 2px 6px rgba(0,0,0,0.15); }
  .portal-card .heading { position: absolute; left: 33px; top: 82px; width: 640px; font-size: 35px; line-height: 30px; }
  .portal-card .body-text { position: absolute; left: 33px; top: 182px; width: 620px;
    font-size: 16px; line-height: 30px; font-weight: 400; }
  .trial { color: var(--accent-red); }
  .cta-lime { background: var(--lime); left: 34px; top: 360px; }

  .reports { top: 1810px; height: 605px;
    background: linear-gradient(90deg, #050606 0%, #1c1e1e 35%, #6c5a48 58%, #8a6a52 72%, #5d6f80 100%); }
  .reports-copy { position: absolute; left: 105px; top: 100px; width: 680px; }
  .reports .heading { font-size: 31px; line-height: 30px; }
  .reports .lede { margin-top: 40px; font-family: "Montserrat", sans-serif; font-weight: 600;
    font-size: 19px; line-height: 30px; }
  .cta-sky { background: var(--sky-blue); left: 105px; top: 361px; }

  .site-footer { position: absolute; left: 0; top: 2415px; width: 1200px; height: 96px; background: #000;
    font-family: "Montserrat", sans-serif; font-weight: 600; font-size: 14px; }
  .copyright { position: absolute; left: 36px; top: 38px; }
  .contact { position: absolute; right: 36px; top: 34px; display: flex; align-items: center; gap: 12px; }
  .social { display: flex; align-items: center; gap: 5px; font-size: 12px; font-weight: 600; }
  .social i { display: inline-block; width: 10px; height: 10px; background: var(--sky-blue); }
</style>
</head>
<body>
  <header class="hero">
    <div class="hero-backdrop" role="img" aria-label="Darkened photo of a woman with closed eyes beside a calm lake"></div>
    <svg class="menu-toggle" viewBox="0 0 36 16" aria-label="Menu">
      <rect x="0" y="0" width="36" height="2" fill="#fff"/>
      <rect x="0" y="7" width="36" height="2" fill="#fff"/>
      <rect x="0" y="14" width="36" height="2" fill="#fff"/>
    </svg>
    <h1 class="hero-title">Harbor Crest Vitality</h1>
    <p class="watch-label">Watch Now</p>
    <svg class="play-button" viewBox="0 0 61 61" aria-label="Play video">
      <circle cx="30.5" cy="30.5" r="30.5" fill="var(--lime)"/>
      <path d="M23 18 L43 30.5 L23 43 Z" fill="#0e1311"/>
    </svg>
    <div class="hero-photo" role="img" aria-label="Photo of a woman meditating cross-legged on a wooden dock by a lake"></div>
  </header>

  <section class="section assess" role="img" aria-label="Photo of a man meditating on a grassy hill at sunset">
    <div class="assess-copy">
      <h2 class="heading">Assess your current Harbor Crest Vitality.</h2>
      <p class="lede">Complete our free life balance assessment to identify key areas where you will most benefit.</p>
    </div>
    <a class="cta cta-ocean" href="#">Learn More</a>
  </section>

  <section class="section portal" role="img" aria-label="Photo of friends jumping joyfully outdoors under a teal sky"></section>
  <div class="portal-card">
    <h2 class="heading">Create a Harbor Crest Vitality learning portal account.</h2>
    <p class="body-text">Get a <span class="trial">14 day free trial</span> to a wealth of learning activities, motivational videos and professional presentations on our learning portal designed specifically to address the eight essential areas of Harbor Crest Vitality.</p>
    <a class="cta cta-lime" href="#">Register Now</a>
  </div>

  <section class="section reports" role="img" aria-label="Photo of a woman seen from behind looking out at the sea">
    <div class="reports-copy">
      <h2 class="heading">Get weekly reports on your progress and goal achievement.</h2>
      <p class="lede">Celebrate your success each week as you review your progress on each life balance area.</p>
    </div>
    <a class="cta cta-sky" href="#">Learn More</a>
  </section>

  <footer class="site-footer">
    <p class="copyright">Copyright © 2020 HarborCrestVitality</p>
    <div class="contact">
      <span>Contact With Us:</span>
      <span class="social"><i></i>Lensly</span>
      <span class="social"><i></i>Circlebook</span>
      <span class="social"><i></i>Chirpline</span>
    </div>
  </footer>
</body>
</html>
```